AI Layout work for Business Cards, Letterhead and Compliment Slip for Award-winning UK Property Deve

No actual logo or corporate identity design work needed here but some skill required to create layouts for business card, letterhead and compliment slip for this award-winning company.
I can provide AI files featuring the company logo and an initial layout of the business card, (6 versions featuring the same design but for different personnel), along with some initial instructions (with possibly more to follow from the client). The finished layouts for each item need to be print-ready in AI format - 8 in all (6 for each business card plus 1 for letterhead and 1 for compliment slip).
I've given this project a 5-day duration but there may be some flexibility built into that depending on client feedback. Hopefully that won't be a problem.
UPDATE:
The client has been very prescriptive about the layout and design of these. To that end, please find 3 additional pdfs that explain what's required.
1.
All BUSINESS CARDS need to be laid out as per the attached AI file (but see latest pdf to check which layout - there are 2 in the original AI file). Use the details in the VEL-contact-details.pdf to create 6 individual AI files, one for each card.
2.
Create 2 additional AI files, one each for the LETTERHEAD and the COMPLIMENT SLIP based on the latest mock-up that I've provided (letterhead-layout-final.pdf)
In all, I need EIGHT individual AI files, 6 for each business card, 1 for the letterhead and 1 for the compliment slip. I'd like to get this done as soon as possible now please.
Target Market(s)
Purchasers of upmarket luxury properties - see here: http://www.velproperties.co.uk
Industry/Entity Type
Business
Requirements
Must have
- Layouts need to be cool, understated and uncluttered.
Nice to have
- Please keep it simple! The actual logo background colour is likely to change (awaiting confirmation from client) but accompanying text detail and font (Deja Vu Sans Condensed) can remain as seen in the files below - for the time being at least! That having been said, I'm open to suggestions.
Should not have
- Nothing extreme or ostentatious please.

```html
<!DOCTYPE html>
<html lang="en">
<head>
<meta charset="utf-8">
<title>VEL Urban Properties – Business Card</title>
<link href="https://fonts.googleapis.com/css2?family=PT+Sans+Narrow:wght@400;700&display=swap" rel="stylesheet">
<style>
  :root {
    --backdrop: #d8dbea;
    --navy: #1c2655;
    --paper: #f7f7f5;
    --ink: #1d1f2a;
    --white: #ffffff;
  }
  html, body {
    margin: 0;
    padding: 0;
    width: 1200px;
    height: 1000px;
    overflow: hidden;
    background: var(--backdrop);
    font-family: "PT Sans Narrow", "Arial Narrow", sans-serif;
  }
  .canvas {
    position: relative;
    width: 1200px;
    height: 1000px;
  }
  .card {
    position: absolute;
    width: 560px;
    height: 320px;
    box-sizing: border-box;
  }
  .card--front {
    left: 170px;
    top: 150px;
    background: var(--navy);
    display: flex;
    align-items: center;
    justify-content: center;
  }
  .card--back {
    left: 470px;
    top: 530px;
    background: var(--paper);
  }
  .brand-name {
    color: var(--white);
    font-weight: 400;
    text-align: center;
    line-height: 1;
  }
  .card--front .brand-name {
    font-size: 78px;
    letter-spacing: 4px;
  }
  .card--front .brand-name span {
    display: block;
    font-size: 26px;
    letter-spacing: 3px;
    margin-top: 12px;
    text-transform: uppercase;
  }
  .brand-block {
    position: absolute;
    left: 0;
    top: 70px;
    width: 215px;
    height: 130px;
    background: var(--navy);
    display: flex;
    align-items: center;
    justify-content: center;
  }
  .brand-block .brand-name {
    font-size: 50px;
    letter-spacing: 3px;
  }
  .brand-block .brand-name span {
    display: block;
    font-size: 16px;
    letter-spacing: 2px;
    margin-top: 8px;
    text-transform: uppercase;
  }
  .address, .contact {
    position: absolute;
    right: 34px;
    text-align: right;
    color: var(--ink);
    font-size: 16px;
    line-height: 1.3;
  }
  .address { top: 26px; }
  .contact { bottom: 34px; }
  .contact b {
    color: var(--navy);
    font-weight: 700;
  }
</style>
</head>
<body>
<main class="canvas">
  <section class="card card--front" aria-label="Business card front">
    <div class="brand-name">VEL<span>Urban Properties</span></div>
  </section>

  <section class="card card--back" aria-label="Business card back">
    <div class="brand-block">
      <div class="brand-name">VEL<span>Urban Properties</span></div>
    </div>
    <address class="address">
      VEL Exclusive Properties Urban Ltd<br>
      27 Orchard Row<br>
      Marlow Vale<br>
      MV4 2QP
    </address>
    <div class="contact">
      <b>t:</b> +44 (0)1632 960418<br>
      <b>e:</b> enquiries@velproperties.co.uk<br>
      <b>w:</b> velproperties.co.uk
    </div>
  </section>
</main>
</body>
</html>
```